New Business Card Design Project

We are a Nationally ranked independent premium furniture retailer, and we want to show that. I am looking for a fresh look, double sided, modern card.. Open to any ideas or designs.

Target Market(s)

Looking to hit men/women 35-50.

Industry/Entity Type

Business

Contact Information for Business Card

Looking for a clean modern look. With that being said, we are wanting to highlight some of the awards that we have received ( Corvane Best 100 and top 16 National Premium, imagines linked). Also need website on card- www.buyvelmora.com, and follow us; facebook, instagram, twitter (small thumbnails work best for those 3) Would like website, social media info, and two awards on backside with some imagery (we are a furniture, mattress and appliance business) and then logo, name, title address on front side

Colors

Designer to choose colors to be used in the design.

Requirements
Must have
• Company name, address, website, two awards, social media ques
Should not have
• cartoons

```html
<!DOCTYPE html>
<html lang="en">
<head>
<meta charset="utf-8">
<title>Velmora Home Furnishings – Business Card</title>
<link rel="stylesheet" href="https://fonts.googleapis.com/css2?family=Roboto:wght@400;500;700&family=Roboto+Condensed:wght@700&display=swap">
<style>
  :root {
    --backdrop: #a9a9a9;
    --card: #f3f3f3;
    --brand-red: #b3232a;
    --ink: #1b1b1b;
    --muted: #505050;
    --rule: #1a1a1a;
    --badge-navy: #1f4a87;
    --badge-grey: #b9b9b9;
  }
  * { margin: 0; padding: 0; box-sizing: border-box; }
  html, body { width: 1200px; height: 960px; overflow: hidden; }
  body { background: var(--backdrop); font-family: "Roboto", Arial, sans-serif; position: relative; }

  .card {
    position: absolute;
    left: 320px;
    width: 600px;
    background: var(--card);
    box-shadow: 0 2px 4px rgba(0,0,0,.35);
  }
  .card--reverse { top: 100px; height: 345px; }
  .card--front { top: 493px; height: 342px; }

  /* Reverse side */
  .award-seal {
    position: absolute; left: 30px; top: 37px;
    width: 122px; height: 122px; border-radius: 50%;
    background: radial-gradient(circle at 40% 35%, #e0484d, var(--brand-red) 70%);
  }
  .award-listing {
    position: absolute; left: 418px; top: 40px;
    width: 146px; height: 118px;
    background: linear-gradient(90deg, var(--badge-grey) 0 38%, var(--badge-navy) 38% 100%);
    border-radius: 3px;
  }
  .wordmark {
    position: absolute;
    color: var(--brand-red);
    font-family: "Roboto Condensed", Arial, sans-serif;
    font-weight: 700;
    line-height: 1;
  }
  .wordmark__name { display: block; }
  .card--reverse .wordmark { left: 212px; top: 64px; }
  .card--reverse .wordmark__name { font-size: 48px; }
  .card--reverse .wordmark__tag { font-size: 15px; padding-left: 50px; display: block; margin-top: 4px; }

  .rule { position: absolute; left: 0; right: 0; height: 1px; background: var(--rule); }
  .rule--top { top: 173px; }
  .rule--bottom { top: 320px; }

  .imagery {
    position: absolute; left: 0; top: 187px; width: 600px; height: 116px;
    display: flex;
  }
  .imagery__panel { height: 100%; }
  .imagery__panel--living { width: 180px; background: linear-gradient(180deg, #d6d2c9, #b59a74); }
  .imagery__panel--appliances { width: 220px; background: linear-gradient(180deg, #8c8c8c, #3a3a3a 60%, #a37a4d); }
  .imagery__panel--bedding { width: 200px; background: linear-gradient(180deg, #e9e5df, #7fb2d8 55%, #e8e2d8); }

  .social {
    position: absolute; top: 309px; left: 258px;
    display: flex; gap: 5px; padding: 0 6px; background: var(--card);
  }
  .social__dot { width: 23px; height: 23px; border-radius: 50%; background: var(--brand-red); }

  /* Front side */
  .card--front .wordmark { left: 55px; top: 50px; }
  .card--front .wordmark__name { font-size: 64px; }
  .card--front .wordmark__tag { font-size: 20px; padding-left: 70px; display: block; margin-top: 6px; }

  .person { position: absolute; left: 55px; top: 212px; }
  .person__name {
    font-family: "Roboto Condensed", Arial, sans-serif; font-weight: 700;
    font-size: 31px; color: var(--brand-red); line-height: 1;
  }
  .person__title { font-size: 14px; font-weight: 500; color: var(--ink); margin-top: 6px; }

  .contact { position: absolute; left: 371px; top: 167px; color: var(--muted); font-size: 14.5px; line-height: 19px; }
  .contact__address { margin-bottom: 8px; }
  .contact__list { list-style: none; }
  .contact__item { display: flex; align-items: center; gap: 8px; }
  .contact__icon { width: 14px; height: 14px; flex: none; fill: var(--brand-red); }
</style>
</head>
<body>

<section class="card card--reverse" aria-label="Card reverse side">
  <div class="award-seal" role="img" aria-label="Best of the best award seal"></div>
  <div class="wordmark">
    <span class="wordmark__name">Velmora</span>
    <span class="wordmark__tag">Home Furnishings</span>
  </div>
  <div class="award-listing" role="img" aria-label="Corvane Best 100 award badge"></div>
  <div class="rule rule--top"></div>
  <div class="imagery">
    <div class="imagery__panel imagery__panel--living" role="img" aria-label="Bright living room with cream sofas"></div>
    <div class="imagery__panel imagery__panel--appliances" role="img" aria-label="Home appliances and electronics"></div>
    <div class="imagery__panel imagery__panel--bedding" role="img" aria-label="Cushioned bed with blue pillows"></div>
  </div>
  <div class="rule rule--bottom"></div>
  <div class="social" aria-label="Follow us">
    <span class="social__dot"></span>
    <span class="social__dot"></span>
    <span class="social__dot"></span>
  </div>
</section>

<section class="card card--front" aria-label="Card front side">
  <div class="wordmark">
    <span class="wordmark__name">Velmora</span>
    <span class="wordmark__tag">Home Furnishings</span>
  </div>
  <div class="person">
    <p class="person__name">DANIEL REYES</p>
    <p class="person__title">CEO/FOUNDER</p>
  </div>
  <div class="contact">
    <p class="contact__address">4120 Alder Court<br>Brightwater, Oregon 97512</p>
    <ul class="contact__list">
      <li class="contact__item">
        <svg class="contact__icon" viewBox="0 0 16 16"><path d="M3.5 1l3 3-1.8 2a9 9 0 0 0 5.3 5.3l2-1.8 3 3-2 2C6.5 14.5 1.5 9.5 1.5 3z"/></svg>
        555 214 7730
      </li>
      <li class="contact__item">
        <svg class="contact__icon" viewBox="0 0 16 16"><path d="M4 0h8v16H4zM5.5 2v10h5V2zM7 13.3h2v1.2H7z" fill-rule="evenodd"/></svg>
        555 309 4186
      </li>
      <li class="contact__item">
        <svg class="contact__icon" viewBox="0 0 16 16"><path d="M4 1h8v4H4zM1 6h14v6h-3v3H4v-3H1zM5 10v4h6v-4z" fill-rule="evenodd"/></svg>
        555 472 6051
      </li>
      <li class="contact__item">
        <svg class="contact__icon" viewBox="0 0 16 16"><path d="M1 3h14v10H1zM2.5 4.5L8 9l5.5-4.5v7h-11z" fill-rule="evenodd"/></svg>
        daniel@buyvelmora.com
      </li>
      <li class="contact__item">
        <svg class="contact__icon" viewBox="0 0 16 16"><path d="M8 1a7 7 0 1 0 0 14A7 7 0 0 0 8 1zm-1 2.5c-1 1-2 1-2.5 2.5S6 8 7 8s1 2 2 2.5 1 2 .5 3A5.5 5.5 0 0 1 7 2.6zm3 .2c.5 1 .3 2 1.3 2.6s1.5 0 2 1A5.5 5.5 0 0 0 10 3.7z"/></svg>
        www.buyvelmora.com
      </li>
    </ul>
  </div>
</section>

</body>
</html>
```